Refresh of a rather different IT outfit website

Our web site is starting to show it's age. You can see the existing site here: www.plumbcorner.net. As a growing company we want to come across as a dynamic collection of IT experts.

We want to update the design so are open to any colour palette and look, but want to retain our current table logo. We use the logo on our business cards but with a white background - see the attached file, so you don't need to keep the brown or the green.

The design should consider the range of browsers that will be looking at the site - so please show how it will look on a wide screen laptop and a 768x1024 tablet.

We want to add some pages about our team and their skills, probably with photos of each person on the team.

This is an uncoded project - the PSD files of the design is required, not coding.
Updates

Thanks everyone for the submissions so far.  It's a holiday day in the UK today but we will get some feedback on the designs so far out to you.

Target Market(s)

Architects and other creative types looking for IT support

Industry/Entity Type

Business

Font styles to use
Serif
Sans Serif

Requirements
Must have
• Must look good on a laptop and an iPad.

```html
<!DOCTYPE html>
<html lang="en">
<head>
<meta charset="utf-8">
<title>plumbcorner – IT Support</title>
<link rel="stylesheet" href="https://fonts.googleapis.com/css2?family=Ubuntu:wght@400;500;700&family=Roboto+Condensed:wght@700&display=swap">
<style>
:root{
  --plum:#8e0a4e;
  --gold:#dbab00;
  --ink:#444;
  --muted:#666;
  --nav:#3d3d3d;
  --sky:#3f8fd8;
  --sky-dark:#1f6fc4;
  --line:#ddd;
}
*{box-sizing:border-box;margin:0;padding:0}
html,body{width:1043px;height:1200px;overflow:hidden}
body{position:relative;background:#fff;font-family:"Ubuntu",sans-serif;color:var(--ink)}
.abs{position:absolute}
.top-rule{left:0;top:0;width:1043px;height:4px;background:var(--gold)}
.brand{left:114px;top:24px;display:flex;align-items:center;gap:14px}
.brand-mark{width:26px;height:26px;background:var(--gold)}
.brand-name{font-size:52px;font-weight:500;color:var(--plum);letter-spacing:-.5px;line-height:1}
.live-chat{left:815px;top:3px;width:114px;height:22px;background:var(--gold);color:var(--plum);font-size:13px;font-weight:500;display:flex;align-items:center;justify-content:center;gap:6px}
.call{right:114px;top:47px;text-align:left;display:flex;gap:8px;align-items:flex-end}
.call small{display:block;color:var(--gold);font-size:12px;margin-left:2px}
.call strong{display:block;color:var(--plum);font-size:22px;font-weight:400}
.nav{left:114px;top:108px;width:815px;height:27px;display:flex;background:linear-gradient(#555,#2f2f2f);border-radius:3px 3px 0 0;overflow:hidden}
.nav a{color:#fff;text-decoration:none;font-size:12px;font-weight:500;display:flex;align-items:center;justify-content:center;border-right:1px solid #222;flex:auto}
.nav a.active{background:var(--gold);color:var(--plum)}
.hero{left:0;top:135px;width:1043px;height:398px;background:linear-gradient(160deg,#6fb3ee,var(--sky) 45%,var(--sky-dark))}
.hero-arrow{width:40px;height:40px;border-radius:50%;background:#1d1d1d;border:2px solid #555;color:#fff;display:flex;align-items:center;justify-content:center;font-size:20px;top:294px}
.band{left:0;top:533px;width:1043px;height:381px;background:linear-gradient(#e6e6e6,#fff 60px,#fff 300px,#ececec)}
.services{left:114px;top:444px;width:815px;height:130px;background:#fff;border:1px solid var(--line)}
.services-tab{left:443px;top:427px;width:157px;height:34px;background:linear-gradient(#fff,#e9e9e9);border-radius:5px 5px 0 0;font-family:"Roboto Condensed",sans-serif;font-size:20px;color:#444;text-align:center;line-height:34px}
.service{top:470px;width:200px;text-align:center;font-size:12.5px;font-weight:500;color:#333}
.service .badge{width:50px;height:50px;border-radius:50%;background:var(--gold);margin:0 auto 18px;display:flex;align-items:center;justify-content:center;box-shadow:0 3px 3px rgba(0,0,0,.2)}
.svc-arrow{top:502px;color:#444;font-size:18px}
.welcome-mark{left:117px;top:598px;width:28px;height:28px;background:var(--gold)}
.welcome-title{left:189px;top:607px;font-size:16px;font-weight:500;color:#333}
.welcome-title span{color:var(--plum);font-size:22px}
.dots{left:114px;top:647px;width:518px;border-top:1px dotted #999}
.welcome-copy{left:116px;top:654px;width:515px;font-size:11.6px;line-height:16.5px;color:var(--muted);letter-spacing:.2px;text-align:justify}
.welcome-copy p{margin-bottom:7px}
.read-more{left:556px;top:767px;color:var(--plum);font-size:12px;font-weight:700}
.video{left:654px;top:610px;width:275px;height:147px;background:linear-gradient(135deg,#ccc,#7a7a7a 50%,#3a3a3a)}
.video-bar{left:654px;top:757px;width:275px;height:14px;background:linear-gradient(#eee,#bbb);font-size:6px;color:#333;display:flex;align-items:center;gap:6px;padding:0 6px}
.news{left:114px;top:835px;width:815px;height:49px;border:1px solid #ccc;border-radius:3px;background:linear-gradient(#fff,#e8e8e8)}
.date{left:127px;top:842px;width:36px;height:36px;text-align:center;color:#fff;font-weight:700}
.date .m{background:var(--gold);font-size:10px;height:14px;line-height:14px}
.date .d{background:var(--plum);font-size:14px;height:22px;line-height:22px}
.news-text{left:207px;top:841px;width:712px;font-size:11.6px;line-height:17px;color:var(--muted)}
.news-text b{color:#555}
.view-all{left:852px;top:864px;color:var(--plum);font-size:11.5px;font-weight:700}
.footer{left:0;top:914px;width:1043px;height:244px;background:var(--plum);color:#fff}
.footer h3{position:absolute;font-weight:400;font-size:16px}
.links{position:absolute;list-style:none;font-size:10.5px}
.links li{height:32px}
.links li::before{content:"›";color:var(--gold);margin-right:10px}
.vrule{position:absolute;top:28px;width:1px;height:140px;background:rgba(255,255,255,.2)}
.field{position:absolute;left:345px;width:208px;background:#fff;border:1px solid #ccc;border-radius:3px;color:#999;font-size:10px;padding:4px 12px}
.btn{position:absolute;background:var(--gold);color:#fff;font-weight:700;font-size:12px;border-radius:2px;text-align:center}
.info{position:absolute;left:596px;font-size:11px;line-height:14px;display:flex;gap:12px}
.info svg{flex:none}
.social{position:absolute;top:1113px;width:22px;height:22px;border-radius:2px}
.copyright{left:0;top:1157px;width:1043px;height:43px;background:var(--gold);color:#222;font-size:12.5px;text-align:center;line-height:43px}
</style>
</head>
<body>
<div class="abs top-rule"></div>

<header>
  <div class="abs brand"><span class="brand-mark"></span><span class="brand-name">plumbcorner</span></div>
  <div class="abs live-chat">
    <svg width="16" height="13" viewBox="0 0 16 13"><ellipse cx="8" cy="6" rx="7" ry="5" fill="none" stroke="#8e0a4e" stroke-width="1.6"/><path d="M3 10 L2 13 L6 10.5" fill="#8e0a4e"/></svg>
    LIVE CHAT
  </div>
  <div class="abs call">
    <svg width="16" height="34" viewBox="0 0 16 34"><path d="M11 2 C4 4 2 12 2 17 C2 22 4 30 11 32 L13 27 C9 25 8 20 8 17 C8 14 9 9 13 7 Z" fill="#222"/></svg>
    <div><small>Call Us</small><strong>020 7946 0123</strong></div>
  </div>
  <nav class="abs nav">
    <a class="active" href="#">HOME</a><a href="#">ABOUT US</a><a href="#">WHAT WE DO</a><a href="#">NEWS BLOG</a><a href="#">ARTICLES</a><a href="#">CLIENTS</a><a href="#">PARTNERS</a><a href="#">CONTACT US</a>
  </nav>
</header>

<div class="abs hero" role="img" aria-label="Businessman drawing a network of cloud services on a blue wall"></div>
<div class="abs hero-arrow" style="left:51px">❮</div>
<div class="abs hero-arrow" style="left:962px">❯</div>

<div class="abs band"></div>

<section>
  <div class="abs services"></div>
  <div class="abs services-tab">Our Services</div>
  <div class="abs svc-arrow" style="left:122px">◀</div>
  <div class="abs svc-arrow" style="left:905px">▶</div>
  <div class="abs service" style="left:134px"><div class="badge"><svg width="26" height="26" viewBox="0 0 26 26"><circle cx="13" cy="13" r="8" fill="none" stroke="#8e0a4e" stroke-width="4" stroke-dasharray="4 2.3"/><circle cx="13" cy="13" r="3" fill="#8e0a4e"/></svg></div>IT Support &amp; Management</div>
  <div class="abs service" style="left:356px"><div class="badge"><svg width="28" height="20" viewBox="0 0 28 20"><path d="M6 19 A6 6 0 0 1 6 8 A8 8 0 0 1 21 6 A6.5 6.5 0 0 1 22 19 Z" fill="#8e0a4e"/><path d="M14 7 L9 12 H12 V17 H16 V12 H19 Z" fill="#dbab00"/></svg></div>Cloud Computing</div>
  <div class="abs service" style="left:553px"><div class="badge"><svg width="24" height="24" viewBox="0 0 24 24"><rect x="2" y="5" width="17" height="12" fill="#8e0a4e"/><rect x="9" y="17" width="3" height="3" fill="#8e0a4e"/><rect x="6" y="20" width="9" height="2" fill="#8e0a4e"/><path d="M19 1 L21 5 L18 4 Z" fill="#8e0a4e"/></svg></div>Disaster Recovery</div>
  <div class="abs service" style="left:738px"><div class="badge"><svg width="24" height="24" viewBox="0 0 24 24"><rect x="3" y="3" width="11" height="11" rx="2" fill="none" stroke="#8e0a4e" stroke-width="3"/><rect x="10" y="10" width="11" height="11" rx="2" fill="none" stroke="#8e0a4e" stroke-width="3"/></svg></div>Virtualisation</div>
</section>

<section>
  <div class="abs welcome-mark"></div>
  <h2 class="abs welcome-title">Welcome to <span>plumbcorner</span></h2>
  <div class="abs dots"></div>
  <div class="abs welcome-copy">
    <p>Plumbcorner was established with a specific aim: to consistently deliver an advanced and comprehensive IT service for ambitious growing companies across many industry sectors. We aim to provide the very best in service and support, and to aid business growth through the effective and skilled use of modern IT solutions</p>
    <p>Founded in 2003, we have grown rapidly and have delivered successful business solutions to small and medium sized businesses, working with customers across a wide IT spectrum. The knowledge, experience and expertise.</p>
  </div>
  <div class="abs read-more">Read more »</div>
  <div class="abs video" role="img" aria-label="Video still of a team joining hands in a circle"></div>
  <svg class="abs" style="left:765px;top:657px" width="56" height="36" viewBox="0 0 56 36"><rect width="56" height="36" rx="6" fill="rgba(60,60,60,.55)"/><path d="M22 9 L36 18 L22 27 Z" fill="#bbb"/></svg>
  <div class="abs video-bar">▶ <span>◂)</span><span>0:00 / 0:47</span><span style="flex:1;height:3px;background:#888;border-radius:2px"></span></div>
</section>

<section>
  <div class="abs news"></div>
  <div class="abs date"><div class="m">AUG</div><div class="d">12</div></div>
  <p class="abs news-text"><b>Duis aute irure dolor</b> in reprehenderit in voluptate velit esse cillum dolore eu fugiat nulla pariatur. Excepteur sint occaecat cupidatat non proident, sunt in culpa qui officia deserunt mollit anim lorem ipsum lorem ispm.</p>
  <div class="abs view-all">View All &gt;&gt;</div>
</section>

<footer class="abs footer">
  <h3 style="left:115px;top:14px">Quick Links</h3>
  <ul class="links" style="left:113px;top:60px"><li>HOME</li><li>ABOUT US</li><li>WHAT WE DO</li><li>NEWS BLOG</li></ul>
  <ul class="links" style="left:220px;top:60px"><li>ARTICLES</li><li>CLIENTS</li><li>PARTNERS</li><li>CONTACT US</li></ul>
  <div class="vrule" style="left:325px"></div>

  <h3 style="left:350px;top:14px">Quick Contact</h3>
  <div class="field" style="top:42px;height:23px">Name</div>
  <div class="field" style="top:71px;height:23px">Email</div>
  <div class="field" style="top:100px;height:41px">Message</div>
  <div class="btn" style="left:345px;top:147px;width:59px;height:20px;line-height:20px">Submit</div>
  <div class="vrule" style="left:573px"></div>

  <h3 style="left:595px;top:14px">Contact Info</h3>
  <div class="info" style="top:53px"><svg width="12" height="14" viewBox="0 0 12 14"><path d="M6 0 A5 5 0 0 1 11 5 C11 9 6 14 6 14 C6 14 1 9 1 5 A5 5 0 0 1 6 0Z" fill="#dbab00"/><circle cx="6" cy="5" r="2" fill="#8e0a4e"/></svg><span>Lorem ipsum dolor sit<br>amet, consectetuer<br>adipiscing elit.</span></div>
  <div class="info" style="top:108px"><svg width="13" height="13" viewBox="0 0 13 13"><circle cx="6.5" cy="6.5" r="5.5" fill="none" stroke="#dbab00" stroke-width="1.4"/><path d="M4.5 3.5 L5.5 6 L7 7.5 L9.5 8.5" fill="none" stroke="#dbab00" stroke-width="1.4"/></svg><span>020 7946 0188</span></div>
  <div class="info" style="top:136px"><svg width="13" height="10" viewBox="0 0 13 10"><rect width="13" height="10" fill="#dbab00"/><path d="M0 0 L6.5 5.5 L13 0" fill="none" stroke="#8e0a4e" stroke-width="1.2"/></svg><span>info@plumbcorner.net</span></div>
  <div class="vrule" style="left:780px"></div>

  <h3 style="left:116px;top:201px">News Letter</h3>
  <div class="field" style="left:228px;top:197px;width:211px;height:26px;font-size:11px;padding:6px 11px">Enter e-mail</div>
  <div class="btn" style="left:375px;top:201px;width:60px;height:19px;line-height:19px">Submit</div>
  <h3 style="left:486px;top:201px">Follow us</h3>
</footer>
<div class="social" style="left:569px;background:#3b5998"></div>
<div class="social" style="left:605px;background:#3aa0d9"></div>
<div class="social" style="left:638px;background:#0a70a8"></div>

<div class="abs copyright">© 2014 plumbcorner. All Rights Reserved.</div>
</body>
</html>
```